Kel Video Games

I need a design for a campaign game, pure news no sale, it fun and modern, and also something different and do it to the other pages there, the design must convey the central idea of ​​the page. You should be able to get on the platform wordpress

Industry/Entity Type

Games

Number of Pages Required

1 page

Font styles to use
Sans Serif

```html
<!DOCTYPE html>
<html lang="en">
<head>
<meta charset="utf-8">
<title>Kel Video Games</title>
<link rel="stylesheet" href="https://fonts.googleapis.com/css2?family=Raleway:wght@400;500;600;700;800&display=swap">
<style>
:root{
  --white:#ffffff;
  --page:#ececec;
  --ink:#222222;
  --muted:#666666;
  --maroon:#6b0f12;
  --accent:#e8442c;
  --orange:#e89a5a;
  --peach:#fbc896;
  --peach-light:#fad8b8;
  --footer:#333333;
  --line:#dddddd;
}
*{box-sizing:border-box;margin:0;padding:0}
html,body{width:1200px;height:2808px;overflow:hidden}
body{font-family:"Raleway",Arial,sans-serif;color:var(--ink);background:var(--page);position:relative}
.abs{position:absolute}
.media{display:block}

/* header */
.site-header{left:0;top:0;width:1200px;height:100px;background:var(--white)}
.brand{left:75px;top:30px;display:flex;align-items:center;gap:10px;font-weight:800;font-size:30px;color:var(--ink);letter-spacing:-0.5px}
.brand-mark{width:30px;height:30px;background:var(--maroon)}
.main-nav{left:365px;top:42px;display:flex;gap:36px;font-size:12px;font-weight:600;color:#444}
.main-nav .active{color:var(--accent)}
.social{left:898px;top:40px;display:flex;gap:16px}
.social span{width:14px;height:14px;border-radius:50%;background:var(--orange)}
.search{left:1106px;top:40px}

/* hero */
.hero{left:0;top:100px;width:1200px;height:558px;background:linear-gradient(135deg,#5c6a78 0%,#2e3842 45%,#1a1f26 70%,#6a4a2a 100%)}
.hero-text{left:75px;top:410px;width:760px;color:var(--white)}
.hero-title{font-size:32px;font-weight:700;margin-bottom:10px}
.hero-meta{font-size:12px;color:var(--orange);margin-bottom:12px}
.hero-excerpt{font-size:14px;line-height:24px}
.hero-arrows{left:1040px;top:452px;display:flex;gap:32px}

/* ad + newsletter */
.banner-ad{left:75px;top:737px;width:690px;height:77px;background:linear-gradient(90deg,#1b2a44,#24304a 60%,#1a1d2a);display:flex;align-items:center;padding:0 22px;color:#7ec4f0}
.banner-name{font-size:38px;font-weight:500;letter-spacing:1px;width:420px}
.banner-copy{font-size:13px;color:#cfd7e6;text-align:right;line-height:18px;flex:1}
.banner-btn{display:inline-block;background:#2e74b8;color:#fff;font-size:8px;padding:1px 8px;border-radius:3px}
.newsletter{left:793px;top:711px;width:333px;height:124px;background:var(--peach);padding:18px 20px}
.newsletter h3{font-size:18px;font-weight:700;color:var(--maroon);text-align:center;margin-bottom:12px}
.newsletter-field{display:flex;height:50px;background:var(--white)}
.newsletter-field span{flex:1;font-size:13px;padding:17px 14px;color:#333}
.newsletter-field b{width:42px;background:#333;display:flex;align-items:center;justify-content:center}

/* featured */
.featured{left:75px;top:878px;display:flex;gap:31px}
.feature{width:330px}
.feature .media{height:173px}
.feature h4{margin-top:18px;font-size:18px;line-height:26px;font-weight:700;color:var(--maroon)}
.rule{left:75px;top:1153px;width:1051px;height:1px;background:#d5d5d5}

/* section heads */
.section-title{font-size:20px;font-weight:600;color:#333;letter-spacing:0.3px}
.view-all{left:972px;top:1183px;width:154px;height:35px;background:var(--peach);font-size:12px;font-weight:700;display:flex;align-items:center;justify-content:center;color:#333}

/* news cards */
.news-grid{left:75px;top:1241px;display:flex;gap:31px}
.news-card{width:330px;height:451px;background:var(--white);position:relative}
.news-card .media{height:200px}
.card-body{padding:12px 20px}
.card-title{font-size:17px;line-height:25px;font-weight:700;color:var(--maroon)}
.card-meta{font-size:11px;color:var(--orange);margin:4px 0 14px}
.card-excerpt{font-size:13px;line-height:23px;color:#444}
.card-stats{position:absolute;left:0;bottom:0;width:100%;height:62px;border-top:1px solid var(--line);display:flex;align-items:center;gap:10px;padding:0 20px;font-size:12px;color:#555}
.card-stats i{display:inline-block;width:12px;height:10px;background:var(--orange);border-radius:2px;margin-right:4px;vertical-align:-1px}

.video-card{left:75px;width:690px;height:262px;background:var(--white)}
.video-card .media{position:absolute;left:22px;top:28px;width:310px;height:200px}
.play{position:absolute;left:135px;top:80px;width:40px;height:40px;border-radius:50%;background:rgba(255,255,255,.85)}
.video-card .card-body{position:absolute;left:360px;top:10px;width:310px;padding:12px 0}
.video-card .card-stats{left:360px;width:310px;height:60px;padding:0;border-top:1px solid var(--line);bottom:0}

/* upcoming */
.upcoming{left:793px;top:1718px;width:333px}
.upcoming-item{display:flex;gap:20px;height:135px;margin-top:0}
.upcoming-item .media{width:122px;height:98px;flex:none}
.upcoming-item h5{font-size:16px;line-height:26px;font-weight:700;color:var(--maroon);margin-top:4px}
.upcoming-item p{font-size:11px;color:var(--orange);margin-top:12px}

/* reviews */
.reviews{left:0;top:2310px;width:1200px;height:333px;background:var(--peach-light)}
.review-arrows{left:746px;top:50px;display:flex;gap:8px}
.review-list{left:75px;top:90px;display:flex;gap:27px}
.review{width:222px}
.review .media{height:140px}
.review h6{font-size:16px;font-weight:700;color:var(--maroon);margin-top:22px}
.stars{margin-top:10px;font-size:13px;color:#555;display:flex;align-items:center;gap:6px}
.side-ad{left:850px;top:50px;width:276px;height:232px;background:linear-gradient(160deg,#3a2a1a,#7a3a14 55%,#d96b1c)}

/* footer */
.site-footer{left:0;top:2643px;width:1200px;height:165px;background:var(--footer);color:#ccc}
.footer-brand{left:75px;top:35px;font-size:24px}
.copyright{left:75px;top:103px;font-size:11px;color:#aaa}
.footer-links{left:618px;top:80px;width:508px;text-align:right;font-size:12px;color:#eee}
</style>
</head>
<body>

<header class="site-header abs">
  <div class="brand abs"><span class="brand-mark"></span>KELGAMES</div>
  <nav class="main-nav abs"><span class="active">HOME</span><span>NEWS</span><span>REVIEWS</span><span>HARDWARE</span><span>PRO BEST OF</span><span>MORE</span></nav>
  <div class="social abs"><span></span><span></span><span></span><span></span><span></span></div>
  <svg class="search abs" width="18" height="18" viewBox="0 0 18 18"><circle cx="7" cy="7" r="5.5" fill="none" stroke="#222" stroke-width="2.2"/><line x1="11" y1="11" x2="16" y2="16" stroke="#222" stroke-width="2.5"/></svg>
</header>

<section class="hero abs" role="img" aria-label="Soldier aiming an assault rifle in the rain with fiery sparks">
  <div class="hero-text abs">
    <h1 class="hero-title">Duis aliquam nibh a dui iaculis viverra id a velit.</h1>
    <p class="hero-meta">By Game Desk, 2 days ago</p>
    <p class="hero-excerpt">Vestibulum ante ipsum primis in faucibus orci luctus et ultrices posuere cubilia lobortis turpis in odio quis nostrud exerci tation ullam.</p>
  </div>
  <svg class="hero-arrows abs" width="100" height="44" viewBox="0 0 100 44"><polyline points="24,4 6,22 24,40" fill="none" stroke="#fff" stroke-width="2.5"/><polyline points="76,4 94,22 76,40" fill="none" stroke="#e8a060" stroke-width="2.5"/></svg>
</section>

<aside class="banner-ad abs">
  <span class="banner-name">NIMBUS</span>
  <span class="banner-copy">Gaming laptops starting<br>at $899<br><span class="banner-btn">Shop now</span></span>
</aside>

<section class="newsletter abs">
  <h3>NEWSLETTER SIGN UP</h3>
  <div class="newsletter-field"><span>Enter Email Address</span><b><svg width="12" height="16" viewBox="0 0 12 16"><polyline points="2,2 9,8 2,14" fill="none" stroke="#fff" stroke-width="2.5"/></svg></b></div>
</section>

<section class="featured abs">
  <article class="feature"><div class="media" role="img" aria-label="Winged healer heroine in white armour" style="background:linear-gradient(135deg,#c9c2b8,#6a625a)"></div><h4>Duis aliquam nibh a dui iaculis viverra id a velit.</h4></article>
  <article class="feature"><div class="media" role="img" aria-label="Mechanical soldiers fighting in a city ruin" style="background:linear-gradient(135deg,#cfd4d8,#6a5a50)"></div><h4>Duis aliquam nibh a dui iaculis viverra id a velit.</h4></article>
  <article class="feature"><div class="media" role="img" aria-label="Team of colourful heroes charging into battle" style="background:linear-gradient(135deg,#3a3f6a,#b05a3a)"></div><h4>Duis aliquam nibh a dui iaculis viverra id a velit.</h4></article>
</section>

<div class="rule abs"></div>
<h2 class="section-title abs" style="left:75px;top:1187px">RECENT NEWS</h2>
<span class="view-all abs">VIEW ALL</span>

<section class="news-grid abs">
  <article class="news-card"><div class="media" role="img" aria-label="Armoured warrior facing a giant stone creature" style="background:linear-gradient(160deg,#4a5560,#1e2228)"></div>
    <div class="card-body"><h3 class="card-title">Duis aliquam nibh a dui iaculis viverra id a velit.</h3><p class="card-meta">By Game Desk, 2 days ago</p><p class="card-excerpt">Vestibulum ante ipsum primis in faucibus orci luctus et ultrices posuere cubilia lobortis turpis in odio...</p></div>
    <div class="card-stats"><span><i></i>23</span>|<span><i></i>21</span></div></article>
  <article class="news-card"><div class="media" role="img" aria-label="Stealth agent with night vision goggles and game title art" style="background:linear-gradient(160deg,#3c4a2a,#111)"></div>
    <div class="card-body"><h3 class="card-title">Duis aliquam nibh a dui iaculis viverra id a velit.</h3><p class="card-meta">By Game Desk, 2 days ago</p><p class="card-excerpt">Vestibulum ante ipsum primis in faucibus orci luctus et ultrices posuere cubilia lobortis turpis in odio...</p></div>
    <div class="card-stats"><span><i></i>23</span>|<span><i></i>21</span></div></article>
  <article class="news-card"><div class="media" role="img" aria-label="Space marine in a red helmet holding a rifle" style="background:linear-gradient(160deg,#5a6468,#2a2a30)"></div>
    <div class="card-body"><h3 class="card-title">Duis aliquam nibh a dui iaculis viverra id a velit.</h3><p class="card-meta">By Game Desk, 2 days ago</p><p class="card-excerpt">Vestibulum ante ipsum primis in faucibus orci luctus et ultrices posuere cubilia lobortis turpis in odio...</p></div>
    <div class="card-stats"><span><i></i>23</span>|<span><i></i>21</span></div></article>
</section>

<article class="video-card abs" style="top:1720px">
  <div class="media" role="img" aria-label="Cutaway view of an underground shelter with rooms" style="background:linear-gradient(160deg,#3a3028,#141414)"><span class="play" style="background:rgba(232,154,90,.9)"></span></div>
  <div class="card-body"><h3 class="card-title">Duis aliquam nibh a dui iaculis viverra id a velit.</h3><p class="card-meta">By Game Desk, 2 days ago</p><p class="card-excerpt">Vestibulum ante ipsum primis in faucibus orci luctus et ultrices posuere cubilia lobortis turpis in odio...</p></div>
  <div class="card-stats"><span><i></i>23</span>|<span><i></i>21</span></div>
</article>
<article class="video-card abs" style="top:2004px">
  <div class="media" role="img" aria-label="Hero aiming a weapon in a colourful fantasy battle" style="background:linear-gradient(160deg,#6a8aa8,#8a5a3a)"><span class="play"></span></div>
  <div class="card-body"><h3 class="card-title">Duis aliquam nibh a dui iaculis viverra id a velit.</h3><p class="card-meta">By Game Desk, 2 days ago</p><p class="card-excerpt">Vestibulum ante ipsum primis in faucibus orci luctus et ultrices posuere cubilia lobortis turpis in odio...</p></div>
  <div class="card-stats"><span><i></i>23</span>|<span><i></i>21</span></div>
</article>

<section class="upcoming abs">
  <h2 class="section-title" style="margin-bottom:18px">TOP UPCOMING GAMES</h2>
  <div class="upcoming-item"><div class="media" role="img" aria-label="Soldier running through a war zone" style="background:linear-gradient(135deg,#4a4a48,#22201e)"></div><div><h5>Viverra id a velit aliquam</h5><p>By Game Desk, 2 days ago</p></div></div>
  <div class="upcoming-item"><div class="media" role="img" aria-label="Tanks advancing across a desert battlefield" style="background:linear-gradient(135deg,#6a5a3a,#2a2418)"></div><div><h5>Viverra id a velit aliquam</h5><p>By Game Desk, 2 days ago</p></div></div>
  <div class="upcoming-item"><div class="media" role="img" aria-label="Armoured fighter in red light" style="background:linear-gradient(135deg,#7a2a2a,#2a1a1a)"></div><div><h5>Viverra id a velit aliquam</h5><p>By Game Desk, 2 days ago</p></div></div>
  <div class="upcoming-item"><div class="media" role="img" aria-label="Soldier in combat gear against a grey sky" style="background:linear-gradient(135deg,#8a9098,#3a3a3a)"></div><div><h5>Viverra id a velit aliquam</h5><p>By Game Desk, 2 days ago</p></div></div>
</section>

<section class="reviews abs">
  <h2 class="section-title abs" style="left:75px;top:48px">REVIEWS</h2>
  <svg class="review-arrows abs" width="50" height="20" viewBox="0 0 50 20"><circle cx="10" cy="10" r="10" fill="#fff"/><polyline points="12,5 7,10 12,15" fill="none" stroke="#e8a060" stroke-width="2"/><circle cx="40" cy="10" r="10" fill="#fff"/><polyline points="38,5 43,10 38,15" fill="none" stroke="#e8a060" stroke-width="2"/></svg>
  <div class="review-list abs">
    <article class="review"><div class="media" role="img" aria-label="Heavy gunner character in a red outfit" style="background:linear-gradient(135deg,#b8542a,#3a2a20)"></div><h6>Duis aliquam nibh</h6><div class="stars"><svg width="86" height="14" viewBox="0 0 86 14" fill="#555"><polygon points="7,0 9,5 14,5 10,8 11.5,13 7,10 2.5,13 4,8 0,5 5,5"/><polygon transform="translate(18 0)" points="7,0 9,5 14,5 10,8 11.5,13 7,10 2.5,13 4,8 0,5 5,5"/><polygon transform="translate(36 0)" points="7,0 9,5 14,5 10,8 11.5,13 7,10 2.5,13 4,8 0,5 5,5"/><polygon transform="translate(54 0)" points="7,0 9,5 14,5 10,8 11.5,13 7,10 2.5,13 4,8 0,5 5,5"/><polygon transform="translate(72 0)" points="7,0 9,5 14,5 10,8 11.5,13 7,10 2.5,13 4,8 0,5 5,5" fill="#999"/></svg>(Fair)</div></article>
    <article class="review"><div class="media" role="img" aria-label="Soldier in blue neon combat scene" style="background:linear-gradient(135deg,#1a2a5a,#b02a3a)"></div><h6>Duis aliquam nibh</h6><div class="stars"><svg width="86" height="14" viewBox="0 0 86 14" fill="#555"><polygon points="7,0 9,5 14,5 10,8 11.5,13 7,10 2.5,13 4,8 0,5 5,5"/><polygon transform="translate(18 0)" points="7,0 9,5 14,5 10,8 11.5,13 7,10 2.5,13 4,8 0,5 5,5"/><polygon transform="translate(36 0)" points="7,0 9,5 14,5 10,8 11.5,13 7,10 2.5,13 4,8 0,5 5,5"/><polygon transform="translate(54 0)" points="7,0 9,5 14,5 10,8 11.5,13 7,10 2.5,13 4,8 0,5 5,5"/><polygon transform="translate(72 0)" points="7,0 9,5 14,5 10,8 11.5,13 7,10 2.5,13 4,8 0,5 5,5" fill="#999"/></svg>(Fair)</div></article>
    <article class="review"><div class="media" role="img" aria-label="Heroine firing a blaster with purple light" style="background:linear-gradient(135deg,#5a3a8a,#d8883a)"></div><h6>Duis aliquam nibh</h6><div class="stars"><svg width="86" height="14" viewBox="0 0 86 14" fill="#555"><polygon points="7,0 9,5 14,5 10,8 11.5,13 7,10 2.5,13 4,8 0,5 5,5"/><polygon transform="translate(18 0)" points="7,0 9,5 14,5 10,8 11.5,13 7,10 2.5,13 4,8 0,5 5,5"/><polygon transform="translate(36 0)" points="7,0 9,5 14,5 10,8 11.5,13 7,10 2.5,13 4,8 0,5 5,5"/><polygon transform="translate(54 0)" points="7,0 9,5 14,5 10,8 11.5,13 7,10 2.5,13 4,8 0,5 5,5"/><polygon transform="translate(72 0)" points="7,0 9,5 14,5 10,8 11.5,13 7,10 2.5,13 4,8 0,5 5,5" fill="#999"/></svg>(Fair)</div></article>
  </div>
  <aside class="side-ad abs" role="img" aria-label="Galaxy Raiders advert: armoured trooper firing a flamethrower, play free today"></aside>
</section>

<footer class="site-footer abs">
  <div class="brand footer-brand abs" style="color:#fff"><span class="brand-mark" style="width:24px;height:24px"></span>KELGAMES</div>
  <p class="copyright abs">Copyright © 2016. Kel Video Games. All Right Reserved</p>
  <p class="footer-links abs">Terms and Conditions &nbsp;/&nbsp; Privacy Policy &nbsp;/&nbsp; Cookies Policy &nbsp;/&nbsp; Advertise with us</p>
</footer>

</body>
</html>
```